Business Cards and Stationery for a laboratory quality consulting business
Brennick Quality Solutions
Creative Brief
Simple
Marion Brennick
Principal Consultant
4817 Thistlewood Lane Cary, NC 27604
marion@brennickquality.example
www.brennickquality.example

```html
<!DOCTYPE html>
<html lang="en">
<head>
<meta charset="utf-8">
<title>Brennick Quality Solutions — Business Card</title>
<link href="https://fonts.googleapis.com/css2?family=Montserrat:wght@500;600;700&display=swap" rel="stylesheet">
<style>
  :root {
    --teal: #0e8280;
    --orange: #f5a01a;
    --green: #6cc11e;
    --paper: #ffffff;
    --bg: #ffffff;
  }
  * { box-sizing: border-box; margin: 0; padding: 0; }
  html, body { width: 1200px; height: 1028px; overflow: hidden; background: var(--bg); }
  body { position: relative; font-family: "Montserrat", Arial, sans-serif; }

  .card {
    position: absolute;
    left: 354px;
    width: 575px;
    height: 329px;
    background: var(--paper);
    overflow: hidden;
  }
  .card--front { top: 152px; }
  .card--back  { top: 572px; }

  .card__accent { position: absolute; left: 0; top: 0; width: 575px; height: 329px; }

  .brand { position: absolute; display: flex; align-items: center; color: var(--teal); font-weight: 700; }
  .brand__dot { border-radius: 50%; background: var(--teal); flex: none; }
  .brand__name { line-height: 1.1; }

  .card--front .brand { left: 8px; top: 22px; gap: 10px; }
  .card--front .brand__dot { width: 36px; height: 36px; }
  .card--front .brand__name { font-size: 19px; }

  .card--back .brand { left: 78px; top: 48px; gap: 16px; }
  .card--back .brand__dot { width: 62px; height: 62px; }
  .card--back .brand__name { font-size: 32px; }

  .person { position: absolute; right: 8px; top: 34px; text-align: right; color: var(--teal); font-weight: 600; font-size: 21px; line-height: 1.25; }

  .contact { position: absolute; left: 4px; top: 139px; color: var(--orange); font-weight: 500; font-size: 14px; line-height: 19.5px; list-style: none; }
</style>
</head>
<body>

<section class="card card--front">
  <svg class="card__accent" viewBox="0 0 575 329" role="img" aria-label="Decorative corner wave in the brand colours">
    <defs>
      <linearGradient id="accent-front" x1="0" y1="0" x2="0" y2="1">
        <stop offset="0" stop-color="#0e8280"/>
        <stop offset="0.55" stop-color="#f5a01a"/>
        <stop offset="1" stop-color="#6cc11e"/>
      </linearGradient>
    </defs>
    <path d="M0 329 C200 290 380 200 575 125 L575 329 Z" fill="url(#accent-front)"/>
  </svg>

  <div class="brand">
    <span class="brand__dot"></span>
    <span class="brand__name">Brennick<br>Quality Solutions</span>
  </div>

  <div class="person">
    <p class="person__name">Marion Brennick</p>
    <p class="person__title">Principal Consultant</p>
  </div>

  <ul class="contact">
    <li>4817 Thistlewood Lane Cary, NC 27604</li>
    <li>Cell: 919-555-0148</li>
    <li>Email: marion@brennickquality.example</li>
    <li>www.brennickquality.example</li>
  </ul>
</section>

<section class="card card--back">
  <svg class="card__accent" viewBox="0 0 575 329" role="img" aria-label="Decorative corner wave in the brand colours">
    <defs>
      <linearGradient id="accent-back" x1="0" y1="0" x2="0" y2="1">
        <stop offset="0" stop-color="#0e8280"/>
        <stop offset="0.55" stop-color="#f5a01a"/>
        <stop offset="1" stop-color="#6cc11e"/>
      </linearGradient>
    </defs>
    <path d="M0 329 C200 295 380 210 575 140 L575 329 Z" fill="url(#accent-back)"/>
  </svg>

  <div class="brand">
    <span class="brand__dot"></span>
    <span class="brand__name">Brennick<br>Quality Solutions</span>
  </div>
</section>

</body>
</html>
```